Young Balance Support Network

We need a poster explaining that some children live with a disability called Vestibular Disorder. Feel free to ask question. We want you to respect our color code, same as our logo.

Here is our website : http://www.ybsnetwork.org/

We need to sensibilise people about this disability for children.

Industry/Entity Type

Charity

Font styles to use
Serif

Requirements
Must have
• 1. our logo (with all our details) + one of the photo of Marek
• 2. design showing a child with a dizziness for exemple
• 3. a title saying : Aidez-nous à changer la vie des enfants vivant avec un problème vestibulaire
• 4.include the text attached (information flyer YBSN)
• Poster size : 24"X 36"
Should not have
• wheel chair

```html
<!DOCTYPE html>
<html lang="fr">
<head>
<meta charset="utf-8">
<title>Young Balance Support Network – Affiche</title>
<link rel="stylesheet" href="https://fonts.googleapis.com/css2?family=Open+Sans:wght@400;600;700;800&display=swap">
<style>
  :root {
    --title-blue: #1b9ccb;
    --heading-navy: #1f3f78;
    --panel-lime: rgba(160, 184, 30, 0.86);
    --pill-blue: rgba(62, 116, 190, 0.88);
    --icon-orange: #f5921e;
    --logo-blue: #2a63ad;
    --white: #ffffff;
  }
  * { margin: 0; padding: 0; box-sizing: border-box; }
  html, body { width: 800px; height: 1200px; overflow: hidden; background: #ffffff; }
  .poster {
    position: relative;
    width: 800px;
    height: 1200px;
    overflow: hidden;
    font-family: "Open Sans", Arial, sans-serif;
  }
  .photo-child {
    position: absolute;
    inset: 0;
    background:
      radial-gradient(ellipse 340px 420px at 230px 560px, #c9a58c 0%, #b08a72 35%, rgba(150,140,135,0) 70%),
      linear-gradient(180deg, #f4f6f7 0%, #e3e6e8 22%, #b9bcbf 55%, #7d7f82 100%);
  }
  .title {
    position: absolute;
    top: 14px;
    left: 20px;
    right: 20px;
    text-align: center;
    color: var(--title-blue);
    font-weight: 800;
    font-size: 47px;
    line-height: 1.14;
    letter-spacing: -0.3px;
  }
  .info-panel {
    position: absolute;
    left: 413px;
    top: 200px;
    width: 362px;
    height: 748px;
    background: var(--panel-lime);
    padding: 22px 24px 20px 26px;
    color: var(--white);
  }
  .info-heading {
    color: var(--heading-navy);
    font-weight: 700;
    font-size: 27px;
    line-height: 1.15;
    text-align: right;
    margin-bottom: 14px;
  }
  .info-heading.second { margin-top: 22px; }
  .info-text {
    font-size: 12px;
    line-height: 1.42;
    margin-bottom: 8px;
  }
  .info-text strong { font-weight: 700; }
  .contact-list {
    position: absolute;
    left: 20px;
    top: 960px;
    list-style: none;
  }
  .contact-item {
    display: flex;
    align-items: center;
    width: 360px;
    height: 58px;
    margin-bottom: 22px;
    background: var(--pill-blue);
    border-radius: 29px;
    color: var(--white);
    font-size: 22px;
    font-weight: 600;
  }
  .contact-icon {
    width: 58px;
    height: 58px;
    border-radius: 50%;
    background: var(--icon-orange);
    display: flex;
    align-items: center;
    justify-content: center;
    margin-right: 18px;
    flex-shrink: 0;
  }
  .logo-card {
    position: absolute;
    left: 482px;
    top: 972px;
    width: 296px;
    height: 204px;
    background: var(--white);
    border-radius: 10px;
    padding: 24px 22px;
    display: flex;
    flex-direction: column;
    justify-content: space-between;
  }
  .logo-name {
    color: var(--logo-blue);
    font-weight: 800;
    font-size: 23px;
    line-height: 1.12;
    text-transform: uppercase;
  }
  .logo-short {
    display: flex;
    align-items: center;
    justify-content: flex-end;
    gap: 12px;
    color: var(--logo-blue);
    font-weight: 800;
    font-size: 30px;
  }
  .logo-dot {
    width: 22px;
    height: 22px;
    border-radius: 50%;
    background: var(--logo-blue);
  }
</style>
</head>
<body>
<main class="poster">
  <div class="photo-child" role="img" aria-label="Photo d'un jeune garçon pris de vertiges, les mains sur les oreilles"></div>

  <h1 class="title">Aidez-nous à changer la vie des enfants vivant avec un problème vestibulaire</h1>

  <section class="info-panel">
    <h2 class="info-heading">Qu'est-ce que le vestibule ?</h2>
    <p class="info-text">C'est un organe sensoriel, pilier de votre équilibre, véritable dôme situé dans l'oreille interne.</p>
    <p class="info-text"><strong>Qu'est-ce qu'une aréflexie vestibulaire ?</strong> C'est l'absence complète de toute information vestibulaire. L'enfant a ainsi l'impression que tout vacille autour de lui, jour et nuit.</p>
    <p class="info-text"><strong>Quelles en sont les conséquences pour l'enfant ?</strong> Le développement moteur de l'enfant est retardé car il doit trouver des solutions afin de construire son équilibre, stabiliser son regard et son corps.</p>
    <p class="info-text">Certains apprentissages sont de véritables obstacles pour l'enfant : se représenter son propre corps, se situer dans l'espace qui l'entoure, interagir avec les autres, communiquer, écrire, lire, manger, boire, marcher. Chacune de ces actions nécessitent des efforts considérables pour se concentrer quelques secondes ou minutes.</p>
    <p class="info-text">Quand l'enfant réussit à effectuer l'une de ces actions, son comportement peut sembler déroutant et bien trop souvent mal interprété par le grand public.</p>

    <h2 class="info-heading second">Quel est le but de notre association ?</h2>
    <p class="info-text">Notre association a pour but de promouvoir les troubles vestibulaires chez l'enfant, ses conséquences sur sa santé ainsi que celle de son entourage et de soutenir ces enfants et leurs parents en leur offrant un espace de parole et des solutions concrètes pour soulager leur quotidien. Notre association a également pour but de financer et promouvoir toute action de recherche scientifique visant à aider les enfants ayant un trouble vestibulaire.</p>
  </section>

  <ul class="contact-list">
    <li class="contact-item">
      <span class="contact-icon">
        <svg width="30" height="30" viewBox="0 0 30 30" fill="none" stroke="#fff" stroke-width="2">
          <circle cx="15" cy="15" r="12"/>
          <ellipse cx="15" cy="15" rx="5.5" ry="12"/>
          <line x1="3" y1="15" x2="27" y2="15"/>
        </svg>
      </span>
      www.ybsnetwork.org
    </li>
    <li class="contact-item">
      <span class="contact-icon">
        <svg width="30" height="24" viewBox="0 0 30 24" fill="none" stroke="#fff" stroke-width="2">
          <rect x="2" y="3" width="26" height="18" rx="2"/>
          <polyline points="2,4 15,14 28,4"/>
        </svg>
      </span>
      info@ybsnetwork.org
    </li>
    <li class="contact-item">
      <span class="contact-icon">
        <svg width="28" height="28" viewBox="0 0 24 24" fill="#fff">
          <path d="M6.6 10.8a15.1 15.1 0 0 0 6.6 6.6l2.2-2.2c.3-.3.7-.4 1-.2 1.1.4 2.3.6 3.6.6.6 0 1 .4 1 1V20c0 .6-.4 1-1 1A17 17 0 0 1 3 4c0-.6.4-1 1-1h3.5c.6 0 1 .4 1 1 0 1.3.2 2.5.6 3.6.1.3 0 .7-.2 1z"/>
        </svg>
      </span>
      14-555010-2
    </li>
  </ul>

  <aside class="logo-card">
    <p class="logo-name">Young Balance<br>Support<br>Network</p>
    <p class="logo-short"><span class="logo-dot"></span>YBSN</p>
  </aside>
</main>
</body>
</html>
```